Visitenkarte erstellen für Reiki Praxis

Visitenkarten für Reiki Praxis Doppelseitig

business cards reiki practice double-sided

The background can also be a different color

```html
<!DOCTYPE html>
<html lang="en">
<head>
<meta charset="utf-8">
<title>Quiet Current Reiki – Business Cards</title>
<link rel="stylesheet" href="https://fonts.googleapis.com/css2?family=Open+Sans:wght@500&family=Montserrat:wght@400&family=Poppins:wght@400;600&display=swap">
<style>
  :root {
    --backdrop: #ece8e6;
    --magenta: #c41560;
    --ink-band: #18171c;
    --gold: #d9b43a;
    --saffron: #e0a922;
    --white: #ffffff;
    --soft-white: #e9e7ea;
    --black: #111111;
  }
  * { margin: 0; padding: 0; box-sizing: border-box; }
  html, body { width: 1200px; height: 1181px; overflow: hidden; }
  body { background: var(--backdrop); position: relative; }

  .card {
    position: absolute;
    width: 655px;
    height: 403px;
    overflow: hidden;
    box-shadow: 0 6px 18px rgba(0,0,0,0.18);
  }
  .card--front { left: 181px; top: 156px; }
  .card--back { left: 480px; top: 627px; background: var(--saffron); }

  .front__brand-band {
    position: absolute; left: 0; top: 0; width: 100%; height: 228px;
    background: var(--magenta);
  }
  .front__info-band {
    position: absolute; left: 0; top: 228px; width: 100%; height: 175px;
    background: var(--ink-band);
  }

  .brand-mark {
    position: absolute;
    left: 50%;
    width: 56px; height: 56px;
    margin-left: -28px;
    border-radius: 50%;
  }
  .card--front .brand-mark { top: 40px; background: var(--gold); }
  .card--back .brand-mark { top: 140px; background: var(--black); }

  .brand-name {
    position: absolute; left: 0; width: 100%;
    text-align: center;
    font-family: 'Open Sans', sans-serif;
    font-weight: 500;
    font-size: 34px;
    line-height: 1;
    letter-spacing: 0.5px;
  }
  .brand-owner {
    position: absolute; left: 0; width: 100%;
    text-align: center;
    font-family: 'Montserrat', sans-serif;
    font-weight: 400;
    font-size: 23px;
    line-height: 1;
    letter-spacing: 8px;
    padding-left: 8px;
  }
  .card--front .brand-name { top: 134px; color: var(--white); }
  .card--front .brand-owner { top: 171px; color: var(--gold); }
  .card--back .brand-name { top: 224px; color: var(--black); }
  .card--back .brand-owner { top: 261px; color: var(--black); }

  .person {
    position: absolute; right: 345px; top: 272px;
    text-align: right;
    font-family: 'Poppins', sans-serif;
  }
  .person__name {
    color: var(--magenta); font-weight: 600; font-size: 24px; line-height: 28px;
  }
  .person__role {
    color: var(--soft-white); font-weight: 400; font-size: 18px; line-height: 20px;
  }
  .divider {
    position: absolute; left: 329px; top: 259px; width: 1px; height: 85px;
    background: #4a4950;
  }
  .contact-list {
    position: absolute; left: 347px; top: 260px;
    list-style: none;
    font-family: 'Poppins', sans-serif;
    font-size: 19px; color: var(--soft-white);
  }
  .contact-list li { display: flex; align-items: center; height: 24px; }
  .contact-list svg { width: 16px; height: 16px; margin-right: 7px; fill: var(--magenta); }
  .address {
    position: absolute; left: 0; width: 100%; top: 347px;
    text-align: center;
    font-family: 'Poppins', sans-serif;
    font-size: 18px; color: var(--soft-white);
  }
</style>
</head>
<body>

<section class="card card--front">
  <div class="front__brand-band"></div>
  <div class="front__info-band"></div>
  <span class="brand-mark"></span>
  <p class="brand-name">QUIET CURRENT REIKI</p>
  <p class="brand-owner">MIRA HOLLEN</p>

  <div class="person">
    <p class="person__name">ELIAS BRANDT</p>
    <p class="person__role">Managing Director</p>
  </div>
  <div class="divider"></div>
  <ul class="contact-list">
    <li><svg viewBox="0 0 16 16"><path d="M1 6c0-2 3-3.5 7-3.5S15 4 15 6v1.5h-3.5V6h-7v1.5H1zM3.5 8h9l1.5 5.5H2z"/></svg>044-987 654 321</li>
    <li><svg viewBox="0 0 16 16"><path d="M1 3h14v10H1zM2.5 4.5 8 9l5.5-4.5v-.1H2.5z" fill-rule="evenodd"/></svg>hello@quietcurrent.example</li>
    <li><svg viewBox="0 0 16 16"><circle cx="8" cy="8" r="7"/><path d="M4 5c2 0 3 1 2 3s1 3 2 4M10 3c0 2 2 2 3 3" stroke="#18171c" stroke-width="1.3" fill="none"/></svg>www.quietcurrent.example</li>
  </ul>
  <p class="address">18, Linden Lane, 10234, Sample Country</p>
</section>

<section class="card card--back">
  <span class="brand-mark"></span>
  <p class="brand-name">QUIET CURRENT REIKI</p>
  <p class="brand-owner">MIRA HOLLEN</p>
</section>

</body>
</html>
```